PowerPoint Design Project for IT Consumerization presentation

I will be giving a presenatation using PP slides. The topic will the Crossover IT is having. I will provide the content for the slides and there will be about 20 slides. I would like for the slides to be professional designed.

It Professional

```html
<!DOCTYPE html>
<html lang="en">
<head>
<meta charset="utf-8">
<title>Crossover IT – slide set</title>
<link rel="stylesheet" href="https://fonts.googleapis.com/css2?family=Archivo+Black&family=PT+Sans:wght@400;700&display=swap">
<style>
:root{
  --page:#e6e3df;
  --slide-top:#ffffff;
  --slide-bottom:#d9d9d9;
  --ink:#2b2b2b;
  --ink-name:#3a3a3a;
  --body:#6a6a6a;
  --band:#0b0b0b;
  --band-grey:#8a8a8a;
  --cell:#f4f4f4;
  --cell-line:#d6d6d6;
  --header-bar:#3c3c3c;
  --photo-a:#3c3648;
  --photo-b:#7d7789;
}
*{margin:0;padding:0;box-sizing:border-box}
html,body{width:1200px;height:689px;overflow:hidden}
body{background:var(--page);position:relative;font-family:"PT Sans",Arial,sans-serif;color:var(--ink)}
.slide{position:absolute;width:253px;height:189px;background:linear-gradient(160deg,var(--slide-top) 0%,var(--slide-bottom) 100%);box-shadow:0 3px 8px rgba(0,0,0,.25);overflow:hidden}
.slide .footer{position:absolute;left:0;bottom:0;width:253px;height:18px}
.slide .url{position:absolute;right:16px;bottom:4px;color:#fff;font-weight:700;font-size:7.5px;letter-spacing:.4px}
.heading{position:absolute;left:23px;top:16px;font-weight:700;font-size:11px;letter-spacing:.2px}
.company{position:absolute;right:14px;top:14px;font-weight:700;font-size:11px;color:var(--ink-name);line-height:1}
.body-text{position:absolute;font-size:5.2px;line-height:1.75;color:var(--body)}
.bullets{position:absolute;list-style:none;font-size:5.8px;font-weight:700;color:var(--ink)}
.bullets li{position:relative;padding-left:9px;margin-bottom:4.6px;line-height:1.2}
.bullets li::before{content:"";position:absolute;left:0;top:1.5px;width:4.5px;height:4.5px;border-radius:50%;background:var(--ink)}
.photo{position:absolute;border:1px solid #555;background:linear-gradient(135deg,var(--photo-a),var(--photo-b))}
.company-big{position:absolute;left:0;width:100%;text-align:center;font-weight:700;font-size:28px;color:var(--ink-name);line-height:1}
.title-block{position:absolute;left:0;width:100%;text-align:center}
.title-block .title{font-weight:700;font-size:14px}
.title-block .desc{font-size:9px;color:var(--ink);margin-top:2px}
.part{position:absolute;left:0;width:100%;text-align:center;font-weight:700;font-size:16px}
.thanks{position:absolute;left:0;width:100%;text-align:center}
.thanks .big{font-family:"Archivo Black",sans-serif;font-size:17px;line-height:1.15}
.thanks .small{font-weight:700;font-size:10.5px}
.table{position:absolute;left:23px;top:32px;width:206px}
.table .bar{background:var(--header-bar);color:#fff;font-weight:700;font-size:8.5px;padding:4px 0 4px 9px}
.table .grid{display:grid;grid-template-columns:repeat(4,1fr);background:var(--cell)}
.table .grid span{font-size:5px;color:var(--body);padding:4px 0 4px 8px;border-bottom:1px solid var(--cell-line);border-right:1px solid var(--cell-line)}
.table .grid span:nth-child(4n){border-right:none}
.columns{position:absolute;left:20px;top:37px;width:218px;display:grid;grid-template-columns:1fr 1fr;column-gap:12px;row-gap:8px}
.columns h4{font-size:5px;font-weight:700;color:var(--ink)}
.columns p{font-size:5px;line-height:1.45;color:var(--body)}
</style>
</head>
<body>

<svg width="0" height="0" style="position:absolute">
  <defs>
    <g id="slide-footer">
      <polygon points="0,6 140,6 136,9 0,9" fill="var(--band-grey)"/>
      <polygon points="0,11 128,11 128,18 0,18" fill="var(--band)"/>
      <polygon points="134,11 145,4 253,4 253,18 126,18" fill="var(--band)"/>
    </g>
    <g id="db">
      <rect x="0" y="3" width="32" height="16" fill="#3a3a3a"/>
      <ellipse cx="16" cy="19" rx="16" ry="3.5" fill="#3a3a3a"/>
      <ellipse cx="16" cy="3" rx="16" ry="3.5" fill="#7a7a7a"/>
      <text x="16" y="15" fill="#fff" font-size="4.5" text-anchor="middle" font-family="PT Sans, sans-serif" font-weight="700">Lorem</text>
    </g>
  </defs>
</svg>

<!-- Row 1 -->
<section class="slide" style="left:333px;top:32px">
  <div class="company-big" style="top:42px">Crossover IT</div>
  <div class="title-block" style="top:98px"><div class="title">TITLE OF PRESENTATION</div><div class="desc">Description</div></div>
  <svg class="footer" viewBox="0 0 253 18"><use href="#slide-footer"/></svg>
  <span class="url">www.itshift-talks.com</span>
</section>

<section class="slide" style="left:604px;top:32px">
  <h2 class="heading">LOREM IPSUM &nbsp;LOREM</h2>
  <span class="company">Crossover IT</span>
  <p class="body-text" style="left:23px;top:41px;width:208px">Lorem ipsum dolor sit amet, consectetur adipiscing elit, sed diam nonummy nibh euismod tincidunt ut laoreet dolore magna aliquam erat volutpat. Ut wisi enim ad minim veniam, quis nostrud exerci tation ullamcorper suscipit lobortis nisl ut aliquip ex ea commodo consequat. Duis autem vel eum iriure dolor in hendrerit in vulputate velit esse molestie consequat, vel illum dolore eu feugiat nulla facilisis.</p>
  <ul class="bullets" style="left:23px;top:101px">
    <li>Lorem ipsum &nbsp;Lorem Lorem ipsum</li>
    <li>Lorem ipsum Lorem Lorem</li>
    <li>Lorem ipsum Lorem Lorem ipsum</li>
    <li>Lorem ipsum orem Lorem ipsum</li>
    <li>Lorem ipsum Lorem</li>
  </ul>
  <div class="photo" role="img" aria-label="Photo of a hand reaching toward a digital screen" style="left:139px;top:94px;width:90px;height:69px"></div>
  <svg class="footer" viewBox="0 0 253 18"><use href="#slide-footer"/></svg>
  <span class="url">www.itshift-talks.com</span>
</section>

<!-- Row 2 -->
<section class="slide" style="left:37px;top:247px">
  <h2 class="heading">LOREM IPSUM &nbsp;LOREM</h2>
  <span class="company">Crossover IT</span>
  <p class="body-text" style="left:23px;top:36px;width:210px">Lorem ipsum dolor sit amet, consectetuer adipiscing elit, sed diam nonummy nibh euismod tincidunt ut laoreet dolore magna aliquam erat volutpat. Ut wisi enim ad minim veniam, quis nostrud exerci tation ullamcorper suscipit lobortis nisl ut aliquip ex ea commodo consequat.</p>
  <div class="photo" role="img" aria-label="Photo of an office workstation with several monitors" style="left:66px;top:84px;width:121px;height:77px"></div>
  <svg class="footer" viewBox="0 0 253 18"><use href="#slide-footer"/></svg>
  <span class="url">www.itshift-talks.com</span>
</section>

<section class="slide" style="left:333px;top:247px">
  <h2 class="heading">LOREM IPSUM</h2>
  <span class="company">Crossover IT</span>
  <p class="body-text" style="left:19px;top:36px;width:136px">Lorem ipsum dolor sit amet, consectetuer adipiscing elit, sed diam nonummy nibh euismod tincidunt ut laoreet dolore magna aliquam erat volutpat. Ut wisi enim ad minim veniam, quis nostrud exerci tation ullamcorper suscipit lobortis nisl ut aliquip ex ea commodo consequat. Duis autem vel eum iriure dolor in hendrerit in vulputate velit esse molestie consequat, vel illum dolore nibh euismod tincidunt ut laoreet dolore magna aliquam erat volutpat.</p>
  <p class="body-text" style="left:19px;top:116px;width:214px">Lorem ipsum dolor sit amet, consectetuer adipiscing elit, sed diam nonummy nibh euismod tincidunt ut laoreet dolore magna aliquam erat volutpat. Ut wisi enim ad minim veniam, quis nostrud exerci tation ullamcorper suscipit lobortis nisl ut aliquip ex ea commodo consequat. Duis autem vel eum.</p>
  <div class="photo" role="img" aria-label="Photo of a person standing beside server racks" style="left:158px;top:37px;width:86px;height:66px"></div>
  <svg class="footer" viewBox="0 0 253 18"><use href="#slide-footer"/></svg>
  <span class="url">www.itshift-talks.com</span>
</section>

<section class="slide" style="left:616px;top:247px">
  <h2 class="heading">LOREM IPSUM</h2>
  <span class="company">Crossover IT</span>
  <div class="table">
    <div class="bar">Lorem ipsum &nbsp;Lorem ipsum &nbsp;Lorem ipsum</div>
    <div class="grid">
      <span>Lorem ipsum</span><span>Lorem ipsum</span><span>Lorem ipsum</span><span>Lorem ipsum</span>
      <span>Lorem ipsum</span><span>Lorem ipsum</span><span>Lorem ipsum</span><span>Lorem ipsum</span>
      <span>Lorem ipsum</span><span>Lorem ipsum</span><span>Lorem ipsum</span><span>Lorem ipsum</span>
      <span>Lorem ipsum</span><span>Lorem ipsum</span><span>Lorem ipsum</span><span>Lorem ipsum</span>
      <span>Lorem ipsum</span><span>Lorem ipsum</span><span>Lorem ipsum</span><span>Lorem ipsum</span>
      <span>Lorem ipsum</span><span>Lorem ipsum</span><span>Lorem ipsum</span><span>Lorem ipsum</span>
      <span>Lorem ipsum</span><span>Lorem ipsum</span><span>Lorem ipsum</span><span>Lorem ipsum</span>
    </div>
  </div>
  <svg class="footer" viewBox="0 0 253 18"><use href="#slide-footer"/></svg>
  <span class="url">www.itshift-talks.com</span>
</section>

<section class="slide" style="left:901px;top:247px">
  <h2 class="heading">LOREM IPSUM</h2>
  <span class="company">Crossover IT</span>
  <svg style="position:absolute;left:0;top:0" width="253" height="189" viewBox="0 0 253 189" font-family="PT Sans, sans-serif" font-weight="700">
    <g stroke="#9a9a9a" stroke-width=".6" fill="none">
      <path d="M30 58 V112 M30 74 H47 M30 108 H47"/>
      <path d="M79 58 V140 M79 74 H98 M79 108 H98"/>
      <path d="M128 58 V140 M128 74 H148 M128 108 H148"/>
      <path d="M178 58 V140 M178 74 H198 M178 108 H198"/>
    </g>
    <g font-size="4.8" fill="#fff" text-anchor="middle">
      <rect x="32" y="40" width="42" height="16" rx="2" fill="#3a3a3a"/><text x="53" y="50">Lorem ipsum</text>
      <rect x="82" y="40" width="42" height="16" rx="2" fill="#3a3a3a"/><text x="103" y="50">Lorem ipsum</text>
      <rect x="132" y="40" width="42" height="16" rx="2" fill="#3a3a3a"/><text x="153" y="50">Lorem ipsum</text>
      <rect x="182" y="40" width="42" height="16" rx="2" fill="#3a3a3a"/><text x="203" y="50">Lorem ipsum</text>
    </g>
    <use href="#db" x="37" y="64"/><use href="#db" x="87" y="64"/><use href="#db" x="137" y="64"/><use href="#db" x="187" y="64"/>
    <use href="#db" x="37" y="97"/><use href="#db" x="87" y="97"/><use href="#db" x="137" y="97"/><use href="#db" x="187" y="97"/>
    <use href="#db" x="87" y="129"/><use href="#db" x="137" y="129"/><use href="#db" x="187" y="129"/>
  </svg>
  <svg class="footer" viewBox="0 0 253 18"><use href="#slide-footer"/></svg>
  <span class="url">www.itshift-talks.com</span>
</section>

<!-- Row 3 -->
<section class="slide" style="left:37px;top:465px">
  <div class="company-big" style="top:24px">Crossover IT</div>
  <div class="part" style="top:80px">PART 3</div>
  <p class="body-text" style="left:22px;top:103px;width:210px;text-align:center">Orem ipsum dolor sit amet, consectetur adipiscing elit, sed diam nonummy nibh euismod tincidunt ut laoreet dolore magna aliquam erat volutpat. Ut wisi enim ad minim veniam, quis nostrud exerci tation ullamcorper suscipit lobortis nisl ut aliquip ex ea commodo consequat. Duis autem vel eum iriure dolor in hendrerit in vulputate velit esse molestie consequat, vel illum dolore eu feugiat nulla facilisis.</p>
  <svg class="footer" viewBox="0 0 253 18"><use href="#slide-footer"/></svg>
  <span class="url">www.itshift-talks.com</span>
</section>

<section class="slide" style="left:329px;top:465px">
  <h2 class="heading">LOREM IPSUM</h2>
  <span class="company">Crossover IT</span>
  <ul class="bullets" style="left:22px;top:38px">
    <li>Lorem ipsum &nbsp;Lorem Lorem ipsum Lorem</li>
    <li>Lorem ipsum Lorem Lorem</li>
    <li>Lorem ipsum Lorem Lorem ipsum &nbsp;Lorem &nbsp;Lorem ipsum</li>
    <li>Lorem ipsum orem Lorem ipsum &nbsp;Lo</li>
    <li>Lorem ipsum Lorem</li>
    <li>Lorem ipsum &nbsp;Lorem Lorem ipsum Lorem</li>
    <li>Lorem ipsum Lorem Lorem</li>
    <li>Lorem ipsum Lorem Lorem ipsum &nbsp;Lorem &nbsp;Lorem ipsum</li>
    <li>Lorem ipsum orem Lorem ipsum &nbsp;Lo</li>
    <li>Lorem ipsum Lorem</li>
  </ul>
  <svg class="footer" viewBox="0 0 253 18"><use href="#slide-footer"/></svg>
  <span class="url">www.itshift-talks.com</span>
</section>

<section class="slide" style="left:616px;top:465px">
  <h2 class="heading">LOREM IPSUM</h2>
  <span class="company">Crossover IT</span>
  <div class="columns">
    <div><h4>Sub Title-1</h4><p>Lorem ipsum dolor sit amet, etuer,Lorem ipsum dolor sit amet, etuer.Lorem ipsum dolor sit amet, etuer.Lorem ipsum dolor</p></div>
    <div><h4>Sub Title-1</h4><p>Lorem ipsum dolor sit amet, etuer,Lorem ipsum dolor sit amet, etuer.Lorem ipsum dolor sit amet, etuer.Lorem ipsum dolor</p></div>
    <div><h4>Sub Title-2</h4><p>Lorem ipsum dolor sit amet, etuer,Lorem ipsum dolor sit amet, etuer.Lorem ipsum dolor sit amet, etuer.Lorem ipsum dolor</p></div>
    <div><h4>Sub Title-2</h4><p>Lorem ipsum dolor sit amet, etuer,Lorem ipsum dolor sit amet, etuer.Lorem ipsum dolor sit amet, etuer.Lorem ipsum dolor</p></div>
    <div><h4>Sub Title-3</h4><p>Lorem ipsum dolor sit amet, etuer,Lorem ipsum dolor sit amet, etuer.Lorem ipsum dolor sit amet, etuer.Lorem ipsum dolor</p></div>
    <div><h4>Sub Title-3</h4><p>Lorem ipsum dolor sit amet, etuer,Lorem ipsum dolor sit amet, etuer.Lorem ipsum dolor sit amet, etuer.Lorem ipsum dolor</p></div>
  </div>
  <svg class="footer" viewBox="0 0 253 18"><use href="#slide-footer"/></svg>
  <span class="url">www.itshift-talks.com</span>
</section>

<section class="slide" style="left:901px;top:465px">
  <div class="company-big" style="top:40px">Crossover IT</div>
  <div class="thanks" style="top:102px"><div class="big">Thank You!</div><div class="small">For your attention</div></div>
  <svg class="footer" viewBox="0 0 253 18"><use href="#slide-footer"/></svg>
  <span class="url">www.itshift-talks.com</span>
</section>

</body>
</html>
```